Responsive webpage design for an exsiting layout (romain catholic church)

Example of content and layout on: [url removed, login to view]

header: "Pastoralraum Birkenhal Ost" and the banners (attachement)
The mainmenu entires will be "Pastoralraum", "Dännlikon", "Dullfeld", "Grenzbach", "Schönerbach", "Waltersau", "Zweckverband".
however new entries may follow.
The submenus are different (like on example page)

We need:
- new design (should not look like the other page)
- responsive design
- the colors and design should be matching for a romain catholic church (liturgical colors)
- the page should be "light" (not too much dark colors, background...)

```html
<!DOCTYPE html>
<html lang="de">
<head>
<meta charset="utf-8">
<title>The Church – Pastoralraum</title>
<link rel="stylesheet" href="https://fonts.googleapis.com/css2?family=Poiret+One&family=Metamorphous&family=Arimo:wght@400&family=Ubuntu:wght@400;500&display=swap">
<style>
:root{
  --accent:#a4ad10;
  --ink:#444;
  --muted:#777;
  --line:#e2e2e2;
  --white:#fff;
  --footer:#3c3c3c;
  --footer-edge:#5a8f95;
  --footer-text:#e8e8e8;
  --footer-sub:#c9c9c9;
  --placeholder:#cacaca;
  --badge:#e4e4e4;
  --badge-edge:#bdbdbd;
}
*{box-sizing:border-box;margin:0;padding:0}
html,body{width:783px;height:1200px;overflow:hidden;background:var(--white)}
body{position:relative;font-family:"Poiret One",sans-serif;color:var(--ink)}
.hero{position:absolute;left:0;top:0;width:783px;height:290px;
  background:
   linear-gradient(90deg,rgba(40,70,20,.85) 0,rgba(40,70,20,0) 14%,rgba(40,70,20,0) 84%,rgba(50,90,25,.9) 100%),
   linear-gradient(180deg,#d8c9a0 0,#d9b46e 30%,#b07a35 55%,#5a3a1c 80%,#2e2418 100%);}
.hero-arrow{position:absolute;top:136px;width:14px;height:18px}
.hero-arrow.prev{left:52px}.hero-arrow.next{left:710px}
.navbar{position:absolute;left:110px;top:0;width:562px;height:36px;background:var(--white);
  display:flex;align-items:center;padding:0 9px}
.brand{font-family:"Metamorphous",serif;font-size:15px;color:#555;margin-right:30px}
.menu{display:flex;gap:16px;list-style:none;font-size:9px;color:#333;font-weight:bold}
.menu .caret{display:inline-block;border-left:3px solid transparent;border-right:3px solid transparent;border-top:3px solid #333;margin-left:4px;vertical-align:middle}
.headline{position:absolute;left:110px;top:261px;width:562px;height:48px;background:var(--white);
  text-align:center;font-size:22px;line-height:48px;color:#666}
.divider{position:absolute;left:130px;top:325px;width:523px;height:1px;
  background:linear-gradient(90deg,transparent,#ccc 20%,#ccc 80%,transparent)}
.badges{position:absolute;left:246px;top:326px;display:flex;gap:13px}
.badges span{width:48px;height:53px;background:var(--badge);border:1px solid var(--badge-edge);border-radius:4px}
.about{position:absolute;left:120px;top:402px;width:543px;text-align:center}
.about h1{font-family:"Metamorphous",serif;font-weight:normal;font-size:19px;color:#444;margin-bottom:6px}
.about p{font-size:10.5px;line-height:14px;color:#555;font-weight:bold}
.sidebar{position:absolute;left:110px;top:496px;width:168px;height:435px;border-right:3px solid #f0f0f0}
.section-title{font-family:"Metamorphous",serif;font-size:11.5px;color:#444;margin-bottom:7px}
.side-menu{list-style:none;border:1px solid var(--line);width:168px;margin-bottom:24px}
.side-menu li{height:26px;line-height:26px;padding-left:9px;font-size:10.5px;font-weight:bold;border-top:1px solid var(--line);color:#555}
.side-menu li:first-child{border-top:0}
.side-menu li.active{background:var(--accent);color:var(--white)}
.event-item{display:flex;gap:14px;margin-bottom:7px}
.thumb{width:45px;height:45px;background:var(--placeholder);border:3px solid #fff;box-shadow:0 0 3px rgba(0,0,0,.25);flex:none}
.event-item p{font-family:"Arimo",sans-serif;font-size:7.5px;line-height:11.5px;color:#555;width:95px}
.testimonial{margin-top:17px}
.testimonial blockquote{border-left:4px solid #eee;padding:4px 0 0 16px;font-family:"Arimo",sans-serif;font-size:10px;line-height:14.5px;color:#555}
.testimonial cite{display:block;font-style:normal;font-size:7.5px;color:#999;margin-top:8px}
.main{position:absolute;left:303px;top:496px;width:370px}
.event-photo{width:370px;height:149px;border:3px solid #fff;box-shadow:0 0 4px rgba(0,0,0,.25);
  background:linear-gradient(180deg,#c9602a 0,#e0992e 40%,#c99a3a 58%,#6d8a2a 72%,#4e7a20 100%)}
.event-text{font-size:10.5px;line-height:14.3px;color:#555;font-weight:bold;margin-top:8px;text-align:justify}
.gallery-title{margin-top:23px}
.gallery{display:grid;grid-template-columns:repeat(4,78px);gap:8px 19px}
.gallery div{height:56px;background:var(--placeholder);border:3px solid #fff;box-shadow:0 0 4px rgba(0,0,0,.2);
  font-family:"Arimo",sans-serif;font-size:7px;color:#999;display:flex;align-items:center;justify-content:center}
.footer{position:absolute;left:0;top:954px;width:783px;height:246px;background:var(--footer);border-top:1px solid var(--footer-edge);font-family:"Ubuntu",sans-serif}
.footer-cols{position:absolute;left:118px;top:18px;display:grid;grid-template-columns:repeat(4,141px)}
.footer h3{font-size:9.5px;font-weight:500;color:var(--white);margin-bottom:3px;line-height:12px}
.footer-item{padding:0 0 9px;margin-bottom:9px;border-bottom:1px solid #4a4a4a;width:124px}
.footer-item:last-child{border-bottom:0;margin-bottom:0;padding-bottom:0}
.footer-item strong{display:block;font-size:8px;line-height:11px;font-weight:400;color:var(--footer-text);white-space:nowrap;margin-bottom:1px}
.footer-item strong::before{content:"›";font-weight:500;margin-right:3px}
.footer-item span{display:block;font-size:6.5px;line-height:13px;color:var(--footer-sub);padding-left:8px;white-space:nowrap}
.footer-bottom{position:absolute;left:118px;top:205px;width:555px;border-top:1px solid #4a4a4a;padding-top:12px;display:flex;align-items:center;font-size:7.5px;color:#ccc}
.footer-bottom .legal{margin-left:10px}
.footer-bottom .copy{margin-left:14px;font-size:6.5px}
.social{margin-left:auto;display:flex;gap:5px}
.social span{width:15px;height:15px;border-radius:3px}
</style>
</head>
<body>
<div class="hero" role="img" aria-label="Abendlicher Blick auf eine Kuppelkirche und Steinbrücke, von grünem Laub eingerahmt"></div>
<svg class="hero-arrow prev" viewBox="0 0 14 18"><path d="M11 2 4 9l7 7" fill="none" stroke="rgba(255,255,255,.6)" stroke-width="3"/></svg>
<svg class="hero-arrow next" viewBox="0 0 14 18"><path d="M3 2l7 7-7 7" fill="none" stroke="rgba(255,255,255,.6)" stroke-width="3"/></svg>

<nav class="navbar">
  <span class="brand">The Church</span>
  <ul class="menu">
    <li>Pastoralraum</li><li>Dännlikon</li><li>Dullfeld</li><li>Grenzbach</li>
    <li>Schönerbach<span class="caret"></span></li><li>Waltersau</li><li>Zweckverband</li>
  </ul>
</nav>

<div class="headline">Alle Gottesdienste im März 2014 auf einen Blick!</div>
<div class="divider"></div>

<div class="badges" aria-label="Gemeinden">
  <span></span><span></span><span></span><span></span><span></span>
</div>

<section class="about">
  <h1>About Us</h1>
  <p>It is a long established fact that a reader will be distracted by the readable content of a page when looking at its layout. The point of using Lorem Ipsum is that it has a more-or-less normal distribution of letters, as opposed to using 'Content here, content here', making it look like readable English. Many desktop publishing packages</p>
</section>

<aside class="sidebar">
  <h2 class="section-title">Right Menu</h2>
  <ul class="side-menu">
    <li class="active">Cras justo odio</li><li>Dapibus ac facilisis in</li><li>Morbi leo risus</li><li>Porta ac consectetur ac</li><li>Vestibulum at eros</li>
  </ul>
  <h2 class="section-title">Upcomming Event</h2>
  <div class="event-item"><div class="thumb"></div><p>It is a long established fact that a reader will be distracted by the readable content</p></div>
  <div class="event-item"><div class="thumb"></div><p>It is a long established fact that a reader will be distracted by the readable content</p></div>
  <div class="testimonial">
    <h2 class="section-title">Tesimonila</h2>
    <blockquote>Lorem ipsum dolor sit amet, consectetur adipiscing elit. Integer posuere erat a ante.by the readable content<cite>— Someone famous in Source Title</cite></blockquote>
  </div>
</aside>

<main class="main">
  <h2 class="section-title">Event</h2>
  <div class="event-photo" role="img" aria-label="Landschaft mit einzelnem Baum und Feldern bei Sonnenuntergang"></div>
  <p class="event-text">It is a long established fact that a reader will be distracted by the readable content of a page when looking at its layout. The point of using Lorem Ipsum is that it has a more-or-less normal distribution of letters, as opposed to using 'Content here, content here', making it look like readable English. Many desktop publishing packages</p>
  <h2 class="section-title gallery-title">Image Gallery</h2>
  <div class="gallery">
    <div>350 x 250</div><div>350 x 250</div><div>350 x 250</div><div>350 x 250</div>
    <div>350 x 250</div><div>350 x 250</div><div>350 x 250</div><div>350 x 250</div>
  </div>
</main>

<footer class="footer">
  <div class="footer-cols">
    <div>
      <h3>Herzogsmatt</h3>
      <div class="footer-item"><strong>Besichtigung Kirche Seehalden</strong><span>Donnerstag, 27.März, 18.30<br>katholisches Kirchgemeindehaus</span></div>
      <div class="footer-item"><strong>Besichtigung Kirche Seehalden</strong><span>Donnerstag, 27.März, 18.30<br>katholisches Kirchgemeindehaus</span></div>
      <div class="footer-item"><strong>Besichtigung Kirche Seehalden</strong><span>Donnerstag, 27.März, 18.30<br>katholisches Kirchgemeindehaus</span></div>
    </div>
    <div>
      <h3>Huttfeld</h3>
      <div class="footer-item"><strong>Besichtigung Kirche Seehalden</strong><span>Donnerstag, 27.März, 18.30<br>katholisches Kirchgemeindehaus</span></div>
      <div class="footer-item"><strong>Besichtigung Kirche Seehalden</strong><span>Donnerstag, 27.März, 18.30<br>katholisches Kirchgemeindehaus</span></div>
    </div>
    <div>
      <h3>Langmatt</h3>
      <div class="footer-item"><strong>Besichtigung Kirche Seehalden</strong><span>Donnerstag, 27.März, 18.30<br>katholisches Kirchgemeindehaus</span></div>
      <div class="footer-item"><strong>Besichtigung Kirche Seehalden</strong><span>Donnerstag, 27.März, 18.30<br>katholisches Kirchgemeindehaus</span></div>
    </div>
    <div>
      <h3>Wangen am Bach</h3>
      <div class="footer-item"><strong>Besichtigung Kirche Seehalden</strong><span>Donnerstag, 27.März, 18.30<br>katholisches Kirchgemeindehaus</span></div>
      <div class="footer-item"><strong>Besichtigung Kirche Seehalden</strong><span>Donnerstag, 27.März, 18.30<br>katholisches Kirchgemeindehaus</span></div>
      <div class="footer-item"><strong>Besichtigung Kirche Seehalden</strong><span>Donnerstag, 27.März, 18.30<br>katholisches Kirchgemeindehaus</span></div>
    </div>
  </div>
  <div class="footer-bottom">
    <span class="legal">Terms of Service Privacy Security</span>
    <span class="copy">© 2013 Company Name. All rights reserved</span>
    <div class="social">
      <span style="background:#3b5ba0"></span><span style="background:#2aa3e0"></span><span style="background:#1c7bb8"></span><span style="background:#cf2030"></span>
    </div>
  </div>
</footer>
</body>
</html>
```